Popup Nightclub Grand Opening Flyer

We need to design a flyer for the grand opening of an upscale, exclusive nightclub called "Lanternfall". The design needs to be chic and exclusive. The background should be black and the text should primarily be white. We like minimalist designs.

Here is the text for the flyer
-
Velvetrope Atlanta Presents

Lanternfall (LOGO)

A Popup Nightclub Experience
For one night Only

Friday, October 18, 2013
Party begins at 9PM

INVITE ONLY

See invitation for location details
(Velvetrope Atlanta logo)

-
Examples we like

http://cdn2-b.brivelpost.com/sites/default/files/styles/image_content_width/hash/3d/fa/1472093815_4471_flyer.jpg?itok=R8kqWm2z

http://api.plovra.com/files/7Kqq-Tr82XXB3pQzJvmtR5HL2W719E4nbRtC6KLd4HsfM8Y2qTDK-VmjwDoNqLX4QBzTHD9nakRbVx3m-Pfq8htc3MDTWr5p4/2zelSaturdays.jpg

http://quenmar.com/wp-content/uploads/yootheme/widgetkit/gallery/2zel/2zel-gen_vroom4-01.jpg

Hi All, one thing that we are seeing that we don't like is on over emphasis on the phrase "a popup nightclub experience" please don't make this the largest thing on the flyer

Target Market(s)

Target market is 25-35 year olds who are affluent (rich) and like luxury brands

Requirements
Must have
• Dark Background
Nice to have
• Velvetrope Logo on the bottom
Modern text that isn't curvy
Should not have
• Curved text

```html
<!DOCTYPE html>
<html lang="en">
<head>
<meta charset="utf-8">
<title>Lanternfall Nightclub – Popup Opening Flyer</title>
<link rel="stylesheet" href="https://fonts.googleapis.com/css2?family=Oswald:wght@600&family=Raleway:wght@200;300;500;600&display=swap">
<style>
  :root{
    --bg-deep:#0d0e10;
    --bg-mid:#25272b;
    --ink:#ffffff;
    --ink-soft:#e4eaf6;
    --ink-cool:#b9c6de;
    --ink-muted:#9ea6b6;
    --rule:rgba(255,255,255,0.28);
    --ring:rgba(255,255,255,0.22);
  }
  *{margin:0;padding:0;box-sizing:border-box}
  html,body{width:816px;height:1200px;overflow:hidden;background:var(--bg-deep)}
  .flyer{
    position:relative;width:816px;height:1200px;overflow:hidden;
    font-family:"Raleway",sans-serif;color:var(--ink);text-align:center;
    font-variant-numeric:lining-nums;
  }
  .backdrop{
    position:absolute;inset:0;
    background:
      radial-gradient(ellipse at 50% 48%, rgba(70,74,82,0.55) 0%, rgba(20,21,24,0) 60%),
      linear-gradient(180deg,var(--bg-mid) 0%,#1a1b1e 45%,var(--bg-deep) 100%);
  }
  .ornament{position:absolute;inset:0}
  .line{position:absolute;left:0;width:100%;line-height:1}
  .presenter{top:56px;font-size:23px;font-weight:500;letter-spacing:1px;color:var(--ink-muted)}
  .presenter strong{font-weight:600}
  .venue-name{top:282px;font-size:72px;font-weight:300;letter-spacing:8px;color:var(--ink)}
  .venue-sub{top:370px;font-size:24px;font-weight:300;letter-spacing:3px;color:var(--ink)}
  .tagline-lead{top:436px;font-size:50px;font-weight:200;letter-spacing:2px;color:var(--ink-soft)}
  .headline{
    font-family:"Oswald",sans-serif;font-weight:600;font-size:60px;letter-spacing:4px;
    background:linear-gradient(180deg,#ffffff 10%,var(--ink-cool) 90%);
    -webkit-background-clip:text;background-clip:text;color:transparent;
  }
  .headline-1{top:502px}
  .headline-2{top:570px}
  .one-night{top:654px;font-size:36px;font-weight:200;color:var(--ink-soft)}
  .one-night strong{font-weight:600;color:var(--ink)}
  .date{top:724px;font-size:40px;font-weight:200;letter-spacing:2px;color:var(--ink-soft)}
  .details{top:876px;font-size:22px;font-weight:500;line-height:30px;color:var(--ink-muted)}
  .details b{color:var(--ink);font-weight:600}
  .host{
    top:1034px;display:flex;justify-content:center;align-items:center;gap:18px;
    font-size:36px;font-weight:500;letter-spacing:4px;color:var(--ink);
  }
  .host-mark{width:30px;height:30px;border-radius:50%;border:3px solid var(--ink-soft);flex:none}
  .location-note{top:1128px;font-size:18px;font-weight:500;letter-spacing:1px;color:var(--ink-muted)}
</style>
</head>
<body>
<main class="flyer">
  <div class="backdrop" role="img" aria-label="Dark weathered wood plank texture background"></div>

  <svg class="ornament" width="816" height="1200" viewBox="0 0 816 1200" aria-hidden="true">
    <line x1="800" y1="18" x2="60" y2="1030" stroke="rgba(255,255,255,0.14)" stroke-width="1.5"/>
    <circle cx="408" cy="560" r="278" fill="none" stroke="var(--ring)" stroke-width="2"/>
    <circle class="brand-dot" cx="408" cy="192" r="52" fill="none" stroke="#e8ecf4" stroke-width="10"/>
    <line x1="205" y1="857" x2="610" y2="857" stroke="var(--rule)" stroke-width="1.5"/>
  </svg>

  <p class="line presenter"><strong>VELVETROPE ATLANTA</strong> PRESENTS</p>

  <h1 class="line venue-name">LANTERNFALL</h1>
  <p class="line venue-sub">NIGHTCLUB</p>

  <p class="line tagline-lead">A POPUP</p>
  <h2 class="line headline headline-1">NIGHTCLUB</h2>
  <h2 class="line headline headline-2">EXPERIENCE</h2>
  <p class="line one-night">FOR <strong>ONE NIGHT</strong> ONLY</p>
  <p class="line date">10.18.13</p>

  <p class="line details">PARTY BEGINS AT <b>9PM</b><br>INVITE ONLY</p>

  <p class="line host"><span class="host-mark" aria-hidden="true"></span>VELVETROPE ATLANTA</p>
  <p class="line location-note">SEE INVITATION FOR LOCATION DETAILS</p>
</main>
</body>
</html>
```